ultra-minimalist business card

front (black background, matte):

tarik b. hosseny
writer | photographer
get@tarikhosseny.com

back (white background, matte):

a picture speaks a thousand words;
a word draws a thousand pictures.

www.tarikhosseny.com

all text should be small (white or silver - as long as it shows against the black - on the front; black or gray - as long as it shows against the white - on the back).

feel free to get creative in terms of arrangement, alignment, and font type, but remember, the overall style is minimalist, so nothing too fancy, please.

thanks.

```html
<!DOCTYPE html>
<html lang="en">
<head>
<meta charset="utf-8">
<title>Tarik B. Hosseny — Business Card</title>
<link rel="stylesheet" href="https://fonts.googleapis.com/css2?family=Montserrat:wght@700&family=Roboto+Condensed:ital,wght@0,400;0,700;1,700&family=Pinyon+Script&display=swap">
<style>
  :root {
    --page: #ffffff;
    --front-ink: #0c0d0f;
    --front-tone: #1b1c1f;
    --name: #ffffff;
    --silver: #a9acae;
    --rule-light: #8d9194;
    --back-paper: #ffffff;
    --back-tone: #e4eaec;
    --quote: #111111;
    --initial: rgba(120, 120, 120, 0.55);
    --rule-dark: #2a2a2a;
    --shadow: rgba(0, 0, 0, 0.18);
  }
  * { margin: 0; padding: 0; box-sizing: border-box; }
  html, body {
    width: 1000px;
    height: 1200px;
    overflow: hidden;
    background: var(--page);
  }
  .sheet { position: relative; width: 1000px; height: 1200px; }

  .card {
    position: absolute;
    left: 91px;
    width: 818px;
    overflow: hidden;
    box-shadow: 6px 10px 22px var(--shadow);
  }
  .card-texture { position: absolute; inset: 0; }

  /* front */
  .card-front { top: 84px; height: 468px; background: var(--front-ink); }
  .card-front .card-texture {
    background: linear-gradient(180deg, var(--front-tone) 0%, var(--front-ink) 55%, var(--front-tone) 100%);
  }
  .name {
    position: absolute;
    left: 24px;
    top: 248px;
    transform-origin: left bottom;
    transform: rotate(-8.6deg);
    font-family: "Montserrat", sans-serif;
    font-weight: 700;
    font-size: 68px;
    letter-spacing: 1px;
    line-height: 1;
    color: var(--name);
    white-space: nowrap;
  }
  .roles {
    position: absolute;
    right: 24px;
    top: 286px;
    font-family: "Roboto Condensed", sans-serif;
    font-weight: 400;
    font-size: 33px;
    color: var(--silver);
    white-space: nowrap;
  }
  .contact-rule {
    position: absolute;
    left: 0;
    right: 0;
    display: flex;
    align-items: center;
    gap: 10px;
    font-family: "Roboto Condensed", sans-serif;
    font-size: 23px;
    white-space: nowrap;
  }
  .contact-rule::before,
  .contact-rule::after { content: ""; flex: 1; height: 2px; }
  .card-front .contact-rule { top: 424px; color: var(--silver); }
  .card-front .contact-rule::before,
  .card-front .contact-rule::after { background: var(--rule-light); }

  /* back */
  .card-back { top: 626px; height: 458px; background: var(--back-paper); }
  .card-back .card-texture {
    background: linear-gradient(180deg, var(--back-paper) 0%, var(--back-paper) 25%, var(--back-tone) 100%);
  }
  .verse { position: absolute; left: 0; right: 0; }
  .verse-line {
    position: absolute;
    left: 0;
    width: 818px;
    height: 170px;
  }
  .verse-line .initial {
    position: absolute;
    left: 38px;
    top: 0;
    font-family: "Pinyon Script", cursive;
    font-size: 190px;
    line-height: 1;
    color: var(--initial);
  }
  .verse-line .words {
    position: absolute;
    left: 112px;
    top: 76px;
    font-family: "Roboto Condensed", sans-serif;
    font-style: italic;
    font-weight: 700;
    font-size: 46px;
    color: var(--quote);
    white-space: nowrap;
  }
  .verse-first { top: 10px; }
  .verse-second { top: 180px; }
  .card-back .contact-rule { top: 414px; color: var(--quote); font-weight: 700; }
  .card-back .contact-rule::before,
  .card-back .contact-rule::after { background: var(--rule-dark); }
</style>
</head>
<body>
<main class="sheet">

  <section class="card card-front" aria-label="Card front">
    <div class="card-texture" role="img" aria-label="Subtle dark diamond texture"></div>
    <h1 class="name">tarik b. hosseny</h1>
    <p class="roles">writer &bull; photographer</p>
    <p class="contact-rule">get@tarikhosseny.com</p>
  </section>

  <section class="card card-back" aria-label="Card back">
    <div class="card-texture" role="img" aria-label="Subtle light diamond texture"></div>
    <div class="verse">
      <p class="verse-line verse-first">
        <span class="initial" aria-hidden="true">A</span>
        <span class="words">picture speaks a thousand words;</span>
      </p>
      <p class="verse-line verse-second">
        <span class="initial" aria-hidden="true">A</span>
        <span class="words">word draws a thousand pictures.</span>
      </p>
    </div>
    <p class="contact-rule">www.tarikhosseny.com</p>
  </section>

</main>
</body>
</html>
```